2 Page Brochure - Commercial Roofing Company

We are looking for a double sided brochure, full color, for our commercial roofing company that tells customers a little bit about the company, what we do, and shows a few pictures.
The brochure would need to have our logo and color scheme that coordinates with that logo.
I have uploaded our logo, some ideas I had, and then the idea list also has our website on there if you'd like to take a look around there for some more ideas.
I have also uploaded some photos we'd like to use.
Page size should be 8.5" x 11".
Target Market(s)
Commercial Property Owners
Other font styles liked:
- Match logo font ideally so it's cohesive, but whatever looks best
Look and feel

```html
<!DOCTYPE html>
<html lang="en">
<head>
<meta charset="utf-8">
<title>K&amp;K Roofing – Commercial Roofing Brochure</title>
<link href="https://fonts.googleapis.com/css2?family=Anton&family=Poppins:wght@400;500;600;700&display=swap" rel="stylesheet">
<style>
:root{
  --orange:#e4561f;
  --dark:#222222;
  --black:#0c0c0c;
  --white:#ffffff;
  --ink:#1d1d1d;
  --backdrop:#b3b3b3;
  --rule:#cfcfcf;
}
*{margin:0;padding:0;box-sizing:border-box}
html,body{width:1200px;height:928px;overflow:hidden;background:var(--backdrop);font-family:"Poppins",sans-serif;color:var(--ink)}
.canvas{position:relative;width:1200px;height:928px}
.page{position:absolute;top:140px;width:501px;height:649px;background:var(--white);overflow:hidden;box-shadow:4px 6px 12px rgba(0,0,0,.25)}
.page--front{left:76px}
.page--back{left:623px}
.abs{position:absolute}
.photo{position:absolute;background:linear-gradient(160deg,#6d6f6c,#3a3b38)}
.orange{color:var(--orange)}
.white{color:var(--white)}

/* FRONT */
.front__darkcol{left:252px;top:0;width:249px;height:649px;background:var(--dark)}
.front__hero-photo{left:0;top:0;width:252px;height:228px;background:linear-gradient(150deg,#5d5a4e 0%,#e9ecef 45%,#c7cbcd 60%,#4a4a42 100%)}
.front__hero-block{left:252px;top:0;width:309px;width:233px;height:229px;background:var(--orange)}
.front__strip{left:485px;top:0;width:16px;height:649px;background:var(--white)}
.logo{left:280px;top:38px;width:150px;text-align:center;font-weight:700;color:var(--white);line-height:1}
.logo__mark{font-size:24px;letter-spacing:1px}
.logo__name{font-size:19px;letter-spacing:1px;margin-top:2px}
.hero__kicker{left:280px;top:102px;font-size:14.5px;font-weight:500;letter-spacing:1.4px;color:var(--white)}
.hero__title{left:280px;top:118px;font-family:"Anton",sans-serif;font-size:33px;line-height:1.08;color:var(--white);letter-spacing:.5px}
.hero__text{left:280px;top:189px;width:196px;font-size:7.6px;line-height:1.25;font-weight:500;color:var(--white)}

.section-title{font-size:9.6px;font-weight:700;line-height:1.25;text-transform:uppercase}
.products__title{left:273px;top:264px}
.products{left:268px;top:296px;width:194px;height:156px;display:grid;grid-template-columns:repeat(3,1fr);grid-template-rows:repeat(3,1fr)}
.product{display:flex;flex-direction:column;align-items:center;justify-content:flex-start;padding-top:4px;font-size:8px;line-height:1.2;text-align:center;color:var(--white);border-color:#8a8a8a;border-style:dashed;border-width:0}
.product:nth-child(-n+6){border-bottom-width:1px}
.product:not(:nth-child(3n)){border-right-width:1px}
.tick{width:11px;height:11px;margin-bottom:4px}
.certs__title{left:273px;top:471px}
.certs{left:273px;top:503px;width:192px;display:grid;grid-template-columns:repeat(3,1fr);gap:3px}
.cert{height:23px;background:var(--white);border-radius:3px}
.call{font-size:9.5px;font-weight:700;color:var(--orange)}
.phone{display:flex;align-items:center;gap:4px;font-size:14.5px;font-weight:600}
.roc{font-size:8px;font-weight:500;color:var(--white);background:var(--orange);padding:1px 6px}
.front .call{left:273px;top:566px}
.front .phone{left:273px;top:580px;color:var(--white)}
.front .roc{left:273px;top:601px}

.about__word{left:52px;top:366px;transform:translate(-50%,-50%) rotate(-90deg);font-size:40px;font-weight:500;letter-spacing:3px;color:transparent;-webkit-text-stroke:1.2px var(--orange);white-space:nowrap}
.about__title{left:87px;top:262px;color:var(--orange)}
.about__rule{left:87px;top:300px;width:118px;height:1px;background:var(--rule)}
.stat{left:87px;top:305px;display:flex;align-items:center;gap:6px}
.stat__num{font-size:31px;font-weight:600;color:var(--orange);line-height:1}
.stat__num sup{font-size:16px}
.stat__text{font-size:7.4px;font-weight:600;line-height:1.2}
.about__text{left:87px;width:125px;font-size:7.4px;line-height:1.2}
.about__text--one{top:356px}
.about__text--two{top:418px}
.round{position:absolute;border-radius:50%;border:1.5px solid var(--orange)}
.about__photo{width:92px;height:92px;top:494px}
.website{left:36px;top:603px;font-size:10.5px;font-weight:600;letter-spacing:4.4px}

/* BACK */
.back__block{left:0;top:0;width:252px;height:210px;background:var(--orange)}
.back__blackcol{left:252px;top:0;width:234px;height:649px;background:var(--black)}
.services__title{left:35px;top:34px;color:var(--white)}
.service{display:flex;align-items:center;gap:7px;font-size:7.6px;font-weight:600;line-height:1.2;color:var(--white)}
.service__icon{width:39px;height:39px;border-radius:50%;background:var(--dark);border:2px solid #3c3c3c;display:flex;align-items:center;justify-content:center;flex:none}
.area__title{left:35px;top:228px;color:var(--orange)}
.area__pill{left:35px;top:247px;width:182px;height:20px;border-radius:4px;background:var(--black);color:var(--white);font-size:7.8px;font-weight:600;display:flex;align-items:center;gap:5px;padding-left:8px}
.back__text{left:35px;width:182px;font-size:7.6px;line-height:1.25}
.back__text--bold{font-weight:600}
.back__rule{left:35px;top:552px;width:182px;height:1px;background:var(--rule)}
.back .call{left:35px;top:566px}
.back .phone{left:35px;top:580px;color:var(--ink)}
.back .roc{left:35px;top:601px}
.other__title{left:277px;top:34px;font-size:9.6px;font-weight:700;color:var(--white)}
.other__photo{width:93px;height:93px}
.other__label{position:absolute;width:80px;height:28px;border-radius:14px;background:var(--orange);color:var(--white);font-size:7.4px;font-weight:600;line-height:1.15;text-align:center;display:flex;align-items:center;justify-content:center;border:1.5px solid #f08a5a}
</style>
</head>
<body>
<div class="canvas">

  <!-- Front page -->
  <section class="page page--front front">
    <div class="abs front__darkcol"></div>
    <div class="photo front__hero-photo" role="img" aria-label="Aerial photo of a commercial building with a white flat roof"></div>
    <div class="abs front__hero-block"></div>
    <div class="abs front__strip"></div>

    <div class="abs logo"><div class="logo__mark">K&amp;K</div><div class="logo__name">ROOFING</div></div>
    <p class="abs hero__kicker">OUR SPECIALTY IS</p>
    <h1 class="abs hero__title">COMMERCIAL<br>ROOFS</h1>
    <p class="abs hero__text">K&amp;K Roofing installs all types of commercial roofing, including low slope like TPO, PVC, and more, to steep slope like shingle, tile, metal, and more.</p>

    <h2 class="abs section-title products__title white">K&amp;K Roofing installs the<br><span class="orange">following products:</span></h2>
    <ul class="abs products">
      <li class="product"><svg class="tick" viewBox="0 0 12 12"><circle cx="6" cy="6" r="6" fill="#e4561f"/><path d="M3.3 6.2l1.8 1.8 3.6-3.7" stroke="#fff" stroke-width="1.4" fill="none"/></svg>TPO</li>
      <li class="product"><svg class="tick" viewBox="0 0 12 12"><circle cx="6" cy="6" r="6" fill="#e4561f"/><path d="M3.3 6.2l1.8 1.8 3.6-3.7" stroke="#fff" stroke-width="1.4" fill="none"/></svg>PVC</li>
      <li class="product"><svg class="tick" viewBox="0 0 12 12"><circle cx="6" cy="6" r="6" fill="#e4561f"/><path d="M3.3 6.2l1.8 1.8 3.6-3.7" stroke="#fff" stroke-width="1.4" fill="none"/></svg>Modified<br>Bitumen</li>
      <li class="product"><svg class="tick" viewBox="0 0 12 12"><circle cx="6" cy="6" r="6" fill="#e4561f"/><path d="M3.3 6.2l1.8 1.8 3.6-3.7" stroke="#fff" stroke-width="1.4" fill="none"/></svg>Silicone<br>Coatings</li>
      <li class="product"><svg class="tick" viewBox="0 0 12 12"><circle cx="6" cy="6" r="6" fill="#e4561f"/><path d="M3.3 6.2l1.8 1.8 3.6-3.7" stroke="#fff" stroke-width="1.4" fill="none"/></svg>Shingle</li>
      <li class="product"><svg class="tick" viewBox="0 0 12 12"><circle cx="6" cy="6" r="6" fill="#e4561f"/><path d="M3.3 6.2l1.8 1.8 3.6-3.7" stroke="#fff" stroke-width="1.4" fill="none"/></svg>Acrylic<br>Coatings</li>
      <li class="product"><svg class="tick" viewBox="0 0 12 12"><circle cx="6" cy="6" r="6" fill="#e4561f"/><path d="M3.3 6.2l1.8 1.8 3.6-3.7" stroke="#fff" stroke-width="1.4" fill="none"/></svg>Metal</li>
      <li class="product"><svg class="tick" viewBox="0 0 12 12"><circle cx="6" cy="6" r="6" fill="#e4561f"/><path d="M3.3 6.2l1.8 1.8 3.6-3.7" stroke="#fff" stroke-width="1.4" fill="none"/></svg>Tile</li>
      <li class="product"><svg class="tick" viewBox="0 0 12 12"><circle cx="6" cy="6" r="6" fill="#e4561f"/><path d="M3.3 6.2l1.8 1.8 3.6-3.7" stroke="#fff" stroke-width="1.4" fill="none"/></svg>Spray<br>Polyurethane<br>Foam</li>
    </ul>

    <h2 class="abs section-title certs__title white">Certified with the following<br><span class="orange">manufacturers:</span></h2>
    <div class="abs certs">
      <div class="cert"></div><div class="cert"></div><div class="cert"></div>
      <div class="cert"></div><div class="cert"></div><div class="cert"></div>
    </div>

    <p class="abs call">CALL US TODAY!</p>
    <p class="abs phone"><svg width="12" height="12" viewBox="0 0 12 12"><circle cx="6" cy="6" r="6" fill="#e4561f"/><path d="M4 3.2l1 1.4-.6.8c.4.9 1.1 1.6 2 2l.8-.6 1.4 1-.5 1C6 8.8 3.2 6 3 4z" fill="#fff"/></svg>602-555-0148</p>
    <p class="abs roc">AZ ROC 512907</p>

    <p class="abs about__word">ABOUT US</p>
    <h2 class="abs section-title about__title">K&amp;K Roofing has<br>been serving Arizona<br>for decades</h2>
    <div class="abs about__rule"></div>
    <div class="abs stat"><span class="stat__num">40<sup>+</sup></span><span class="stat__text">Years of installing<br>quality roofs<br>across Arizona</span></div>
    <p class="abs about__text about__text--one">Originally founded in 1984, K&amp;K Roofing has been roofing across Arizona for decades, including schools, retail shopping centers, industrial buildings, and all other types of commercial buildings.</p>
    <p class="abs about__text about__text--two">We are familiar with all types of roofing systems across the many different climate zones of Arizona and would love to work with you on your project to come up with a long term solution.</p>
    <div class="photo round about__photo" style="left:36px;background:linear-gradient(180deg,#4f86c6 0%,#8fb3d8 35%,#c9cfd2 55%,#e9ebec 100%)" role="img" aria-label="Photo of a white coated flat roof with rooftop vents"></div>
    <div class="photo round about__photo" style="left:136px;background:linear-gradient(180deg,#5b95d4 0%,#a9c6e4 45%,#5f8f7c 70%,#3e6f5c 100%)" role="img" aria-label="Photo of a green standing seam metal roof"></div>
    <p class="abs website">www.<span class="orange">kk-roofing</span>.com</p>
  </section>

  <!-- Back page -->
  <section class="page page--back back">
    <div class="abs back__block"></div>
    <div class="abs back__blackcol"></div>

    <h2 class="abs section-title services__title">K&amp;K Roofing offers the<br>following services:</h2>
    <div class="abs service" style="left:35px;top:67px"><span class="service__icon"><svg width="20" height="20" viewBox="0 0 20 20" fill="none" stroke="#fff" stroke-width="1.2"><path d="M2 10L10 3l8 7"/><path d="M5 8v9h10V8"/><path d="M8 17v-5h4v5"/></svg></span>New Roof<br>Installation</div>
    <div class="abs service" style="left:140px;top:67px"><span class="service__icon"><svg width="20" height="20" viewBox="0 0 20 20" fill="none" stroke="#fff" stroke-width="1.2"><path d="M2 14L6 5h8l4 9z"/><path d="M4 10h12M8 5l-2 9M12 5l2 9"/></svg></span>Re-roofing</div>
    <div class="abs service" style="left:35px;top:111px"><span class="service__icon"><svg width="20" height="20" viewBox="0 0 20 20" fill="none" stroke="#fff" stroke-width="1.2"><path d="M2 10L10 3l8 7"/><path d="M5 8v9h6"/><circle cx="13" cy="12" r="3"/><path d="M15 14l3 3"/></svg></span>Roof<br>Inspections</div>
    <div class="abs service" style="left:140px;top:111px"><span class="service__icon"><svg width="20" height="20" viewBox="0 0 20 20" fill="none" stroke="#fff" stroke-width="1.2"><rect x="3" y="4" width="14" height="12"/><path d="M3 8h14M3 12h14M7.7 4v12M12.3 4v12"/></svg></span>Roof<br>Coatings</div>
    <div class="abs service" style="left:35px;top:156px"><span class="service__icon"><svg width="20" height="20" viewBox="0 0 20 20" fill="none" stroke="#fff" stroke-width="1.2"><path d="M2 14L6 5h8l4 9z"/><circle cx="12" cy="9" r="2.5"/><path d="M5 17l5-5"/></svg></span>Roof<br>Maintenance<br>and Service</div>

    <h2 class="abs section-title area__title">Service Area</h2>
    <div class="abs area__pill"><svg width="8" height="10" viewBox="0 0 8 10"><path d="M4 0a3.6 3.6 0 0 0-3.6 3.6C.4 6.3 4 10 4 10s3.6-3.7 3.6-6.4A3.6 3.6 0 0 0 4 0z" fill="#e4561f"/><circle cx="4" cy="3.6" r="1.3" fill="#0c0c0c"/></svg>We service the entire state of Arizona</div>
    <p class="abs back__text" style="top:281px">K&amp;K Roofing opened the doors in 1984, and we've since installed, serviced, maintained, and coated thousands of commercial roofs around the state of Arizona, in the many climate regions of the state.</p>
    <p class="abs back__text" style="top:340px">Though we all live here for the constant sunshine, Arizona is one of the harshest environments in the US for roofs. Constant sun, heat, dryness, and then the torrential monsoon downpours all test the limits of your roof.</p>
    <p class="abs back__text" style="top:408px">We work with you to come up with a solution that works for your roof and will keep your business dry for years to come. Then, our team of project managers, superintendents, foremen, and field workers all come together to execute on that plan and install a quality roof.</p>
    <p class="abs back__text back__text--bold" style="top:487px">We are certified with many different manufacturers, so we're able to offer custom solutions to solve your issues, that will also often come with reputable manufacturer warranties.</p>
    <div class="abs back__rule"></div>
    <p class="abs call">CALL US TODAY!</p>
    <p class="abs phone"><svg width="12" height="12" viewBox="0 0 12 12"><circle cx="6" cy="6" r="6" fill="#e4561f"/><path d="M4 3.2l1 1.4-.6.8c.4.9 1.1 1.6 2 2l.8-.6 1.4 1-.5 1C6 8.8 3.2 6 3 4z" fill="#fff"/></svg>602-555-0148</p>
    <p class="abs roc">AZ ROC 512907</p>

    <h2 class="abs other__title">OTHER <span class="orange">SERVICES:</span></h2>

    <div class="photo round other__photo" style="left:274px;top:58px;background:linear-gradient(180deg,#8a8a86,#e6e6e3 55%,#d0d0cc)" role="img" aria-label="Photo of a TPO membrane being welded on a roof"></div>
    <div class="other__label" style="left:279px;top:148px">TPO Roofing</div>
    <div class="photo round other__photo" style="left:374px;top:58px;background:linear-gradient(180deg,#bdbdb8,#dcdcd8)" role="img" aria-label="Photo of a PVC roof surface"></div>
    <div class="other__label" style="left:379px;top:148px">PVC Roofing</div>

    <div class="photo round other__photo" style="left:274px;top:198px;background:linear-gradient(180deg,#7a8494,#343a40 55%,#25292d)" role="img" aria-label="Photo of a black EPDM roof with skylights"></div>
    <div class="other__label" style="left:279px;top:288px">EPDM Roofing</div>
    <div class="photo round other__photo" style="left:374px;top:198px;background:linear-gradient(180deg,#545750,#777a70 50%,#5d5f57)" role="img" aria-label="Photo of a granulated modified bitumen roof"></div>
    <div class="other__label" style="left:379px;top:288px">Modified<br>Bitumen Roofing</div>

    <div class="photo round other__photo" style="left:274px;top:346px;background:linear-gradient(150deg,#c98f6d,#b9795a 50%,#d9a88a)" role="img" aria-label="Photo of a foam roof with coating"></div>
    <div class="other__label" style="left:279px;top:436px">Roof Coatings</div>
    <div class="photo round other__photo" style="left:374px;top:346px;background:linear-gradient(180deg,#7fa7cf,#5b6f5f 45%,#2f3a3b)" role="img" aria-label="Photo of a building with a standing seam metal roof"></div>
    <div class="other__label" style="left:379px;top:436px">Standing Seam<br>Metal Roofing</div>

    <div class="photo round other__photo" style="left:274px;top:490px;background:linear-gradient(160deg,#5c6068,#7c818a 50%,#4b4e55)" role="img" aria-label="Photo of an asphalt shingle roof"></div>
    <div class="other__label" style="left:279px;top:580px">Asphalt Shingle<br>Roofing</div>
    <div class="photo round other__photo" style="left:374px;top:490px;background:linear-gradient(180deg,#d7d7d4,#ecece9 60%,#cfcfcb)" role="img" aria-label="Photo of a light coloured tile roof"></div>
    <div class="other__label" style="left:379px;top:580px">Tile Roofing</div>
  </section>

</div>
</body>
</html>
```